Brinford Vet Core Values

Brinford Veterinary Services is both a small and large animal practice so we mainly work with cats, dogs, and cows. We want the sign to reflect all three of those animals as well as elements of farm/country life like barns and tractors. We're located in a small town, less then 4,000 people, so we would like the design to have a rural look and feel. We want to use a "rustic" color palette, follow the link to see what we have in mind https://www.palomercoatings.example/homeowners/color/find-and-explore-colors/paint-colors-by-collection/lifestyle-collection/toasted-meadow.
The text we want have appear on the sign is listed below. We also want to C in compassionate, the A in Always, the R in Ready, the E in Expanding, and the S in Service to be bold and standout since they will spell out cares.
"Brinford Veterinary Services is committed to Compassionate and honest care for all patients and clients. This means we are Always efficient with our resources to pass the savings on to our clients. We are also Ready to help with the best medicine available while Expanding to help more of our practice’s families and farms. This is how we provide Service in abundance to all our clients so they are proud to send their family and friends to see us. Brinford Vet CARES."

```html
<!DOCTYPE html>
<html lang="en">
<head>
<meta charset="utf-8">
<title>Brinford Vet Core Values</title>
<link rel="stylesheet" href="https://fonts.googleapis.com/css2?family=Alfa+Slab+One&family=Sorts+Mill+Goudy&family=Yellowtail&display=swap">
<style>
  :root {
    --green: #1f3a2b;
    --paper: #f5f5f5;
    --pattern: #ebebeb;
    --stage: #e4e4e4;
    --white: #ffffff;
  }
  * { margin: 0; padding: 0; box-sizing: border-box; }
  html, body {
    width: 1200px; height: 800px; overflow: hidden;
    background: var(--stage);
  }
  .sign {
    position: absolute; left: 20px; top: 153px;
    width: 1160px; height: 494px;
    background: var(--paper);
    color: var(--green);
    font-family: "Sorts Mill Goudy", Georgia, serif;
  }
  .sign__pattern {
    position: absolute; inset: 0;
    background: var(--pattern);
  }
  .sign__frame-outer {
    position: absolute; inset: 12px;
    border: 4px solid var(--green);
  }
  .sign__frame-inner {
    position: absolute; inset: 23px;
    border: 2px solid var(--green);
  }
  .quote-mark {
    position: absolute;
    font-family: "Alfa Slab One", Georgia, serif;
    font-size: 62px; line-height: 1;
    color: var(--green);
  }
  .quote-mark--open { left: 54px; top: 40px; }
  .quote-mark--close { left: 793px; top: 382px; }
  .values {
    position: absolute; left: 95px; top: 52px; width: 980px;
    text-align: center;
    font-size: 27px; line-height: 44.5px;
    word-spacing: 1px;
  }
  .values__name {
    font-family: "Yellowtail", cursive;
    font-size: 34px;
  }
  .initial {
    display: inline-block;
    width: 38px; height: 36px; line-height: 33px;
    margin: 0 2px 0 4px;
    vertical-align: -5px;
    background: var(--green);
    color: var(--white);
    border: 2px solid var(--white);
    outline: 2px solid var(--green);
    border-radius: 4px;
    font-family: "Alfa Slab One", Georgia, serif;
    font-size: 26px; text-align: center;
  }
  .divider {
    position: absolute; left: 90px; top: 376px;
    width: 988px; height: 1.5px; background: var(--green);
  }
  .divider__ornament {
    position: absolute; left: 548px; top: 366px;
    width: 72px; height: 20px;
    background: var(--paper);
  }
  .divider__ornament span {
    display: block; margin: 7px auto 0;
    width: 62px; height: 6px; border-radius: 3px;
    background: #7d8b82;
  }
  .signoff {
    position: absolute; left: 0; top: 398px; width: 1160px;
    text-align: center;
    font-family: "Sorts Mill Goudy", Georgia, serif;
    font-size: 36px; line-height: 50px;
    color: var(--green);
  }
</style>
</head>
<body>
  <main class="sign">
    <div class="sign__pattern" role="img" aria-label="Soft grey diamond lattice background pattern"></div>
    <div class="sign__frame-outer"></div>
    <div class="sign__frame-inner"></div>

    <span class="quote-mark quote-mark--open">&ldquo;</span>

    <p class="values">
      <span class="values__name">Brinford Veterinary Services</span> is committed to <span class="initial">C</span>ompassionate&nbsp; and honest<br>
      care for all patients and clients.&nbsp; This means we are <span class="initial">A</span>lways efficient with<br>
      our resources to pass the savings on to our clients. We are also <span class="initial">R</span>eady to<br>
      help with the best medicine available while <span class="initial">E</span>xpanding to help more of<br>
      our practice’s families and farms. This is how we provide <span class="initial">S</span>ervice in<br>
      abundance to all our clients so they are proud to send their<br>
      family and friends to see us.
    </p>

    <div class="divider"></div>
    <div class="divider__ornament" role="img" aria-label="Small decorative flourish on the divider line"><span></span></div>

    <p class="signoff">Brinford Vet CARES</p>

    <span class="quote-mark quote-mark--close">&rdquo;</span>
  </main>
</body>
</html>
```